Quillbrook
Quillbrook - Construction
Professional
Dale
Partner
4821 Fennmoor Ave Charlotte, NC 28391
d_q7@zentramail.net
Harriet7 Harriet7
Please use the most current design. you may remove demolition and remediation but please keep the slogan
Can you change construction to Demolition & Remediation?

```html
<!DOCTYPE html>
<html lang="en">
<head>
<meta charset="utf-8">
<title>Quillbrook Business Card</title>
<link href="https://fonts.googleapis.com/css2?family=Open+Sans:wght@400;600;800&display=swap" rel="stylesheet">
<style>
  :root {
    --navy: #1f3566;
    --green: #7dc242;
    --white: #ffffff;
    --backdrop: #e9e7e3;
    --ink-soft: #2b3f6e;
  }
  * { margin: 0; padding: 0; box-sizing: border-box; }
  html, body {
    width: 1200px; height: 901px; overflow: hidden;
    background: var(--backdrop);
    font-family: "Open Sans", Arial, sans-serif;
  }
  .stage {
    position: relative; width: 1200px; height: 901px;
    display: flex; flex-direction: column; align-items: center; justify-content: center; gap: 36px;
  }
  .card {
    position: relative; width: 700px; height: 400px;
    background: var(--white); overflow: hidden;
    box-shadow: 0 6px 18px rgba(0,0,0,0.18);
  }
  .card-shapes { position: absolute; inset: 0; }
  .brand {
    position: absolute; display: flex; flex-direction: column; align-items: flex-start;
  }
  .brand-name {
    display: flex; align-items: center; gap: 10px;
    font-weight: 800; color: var(--navy); font-size: 44px; line-height: 1;
  }
  .brand-square { width: 22px; height: 22px; background: var(--green); }
  .brand-services {
    margin-top: 8px; margin-left: 32px;
    font-weight: 600; font-size: 9px; line-height: 1.35; color: var(--ink-soft);
    list-style: none;
  }
  .card-front .brand { left: 50%; top: 50%; transform: translate(-50%, -50%); }
  .card-back .brand { left: 190px; top: 28px; }
  .card-back .brand-name { font-size: 34px; }
  .card-back .brand-square { width: 17px; height: 17px; }
  .holder { position: absolute; left: 62px; top: 268px; color: var(--white); }
  .holder-name { font-weight: 800; font-size: 44px; line-height: 1; }
  .holder-role { font-weight: 400; font-size: 17px; margin-top: 6px; }
  .contact {
    position: absolute; left: 470px; top: 178px; color: var(--white);
    font-size: 15px; line-height: 1.35; font-style: normal;
  }
  .contact-email { margin-top: 14px; }
</style>
</head>
<body>
<main class="stage">
  <section class="card card-front">
    <div class="brand">
      <div class="brand-name"><span class="brand-square"></span>Quillbrook</div>
      <ul class="brand-services">
        <li>Site Services</li>
        <li>Crane &amp; Rigging</li>
        <li>Asset Recovery</li>
        <li>Remediation</li>
        <li>Demolition</li>
      </ul>
    </div>
  </section>

  <section class="card card-back">
    <svg class="card-shapes" width="700" height="400" viewBox="0 0 700 400">
      <polygon points="0,150 319,345 300,400 0,400" fill="var(--green)"/>
      <polygon points="440,0 700,0 700,400 300,400" fill="var(--navy)"/>
    </svg>
    <div class="brand">
      <div class="brand-name"><span class="brand-square"></span>Quillbrook</div>
      <ul class="brand-services">
        <li>Site Services</li>
        <li>Crane &amp; Rigging</li>
        <li>Asset Recovery</li>
        <li>Remediation</li>
        <li>Demolition</li>
      </ul>
    </div>
    <div class="holder">
      <p class="holder-name">Dale</p>
      <p class="holder-role">Partner</p>
    </div>
    <address class="contact">
      <p>4821 Fennmoor Ave</p>
      <p>Charlotte, NC 28391</p>
      <p class="contact-email">d_q7@zentramail.net</p>
    </address>
  </section>
</main>
</body>
</html>
```